Sports Betting Business Consultant

After 21 years in corporate life. Will be continue as consultant/advisor in sports betting industry. Need a business card. Prefer an Zelvo format as layout. Elements; betting,ticket, sports types soccer, basketball, tennis etc , odds etc.

```html
<!DOCTYPE html>
<html lang="en">
<head>
<meta charset="utf-8">
<title>Deniz Arkan – Sports Advisor Business Card</title>
<link href="https://fonts.googleapis.com/css2?family=Lato:wght@300;400;700;900&display=swap" rel="stylesheet">
<style>
  :root {
    --backdrop: #2b2b2c;
    --card: #1c1d1f;
    --art-tone: #353638;
    --art-tone-soft: #2a2b2d;
    --name: #ffffff;
    --title: #8c8d90;
    --contact: #c9cacc;
    --rule: #4a4b4e;
    --icon-bg: #d9d9d9;
  }
  * { box-sizing: border-box; margin: 0; padding: 0; }
  html, body {
    width: 1200px;
    height: 1108px;
    overflow: hidden;
    background: var(--backdrop);
    font-family: "Lato", sans-serif;
  }
  .stage {
    position: relative;
    width: 1200px;
    height: 1108px;
  }
  .card {
    position: absolute;
    top: 214px;
    width: 420px;
    height: 680px;
    background: var(--card);
    border-radius: 22px;
    box-shadow: 0 10px 30px rgba(0,0,0,0.35);
    overflow: hidden;
  }
  .card--front { left: 150px; }
  .card--back { left: 630px; }

  .sports-art {
    position: absolute;
    border-radius: 40% 45% 40% 50%;
    background: radial-gradient(ellipse at center, var(--art-tone) 0%, var(--art-tone-soft) 60%, rgba(28,29,31,0) 78%);
  }
  .card--front .sports-art {
    left: 80px; top: 60px; width: 260px; height: 280px;
  }
  .card--back .sports-art {
    left: 45px; top: 160px; width: 330px; height: 380px;
  }

  .identity {
    position: absolute;
    left: 0; right: 0; top: 370px;
    text-align: center;
  }
  .identity__name {
    color: var(--name);
    font-weight: 900;
    font-size: 34px;
    letter-spacing: 0.5px;
    line-height: 1.05;
  }
  .identity__title {
    color: var(--title);
    font-weight: 400;
    font-size: 25px;
    line-height: 1.2;
    margin-top: 2px;
  }

  .divider {
    position: relative;
    width: 240px;
    height: 1px;
    background: var(--rule);
    margin: 26px auto 0;
  }
  .divider__icons {
    position: absolute;
    left: 50%; top: -12px;
    transform: translateX(-50%);
    display: flex;
    gap: 4px;
    background: var(--card);
    padding: 0 4px;
  }
  .divider__icons svg { display: block; }

  .contact {
    text-align: center;
    color: var(--contact);
    font-size: 25px;
    line-height: 1.32;
    margin-top: 20px;
  }
  .divider--plain { margin-top: 18px; }

  .services {
    text-align: center;
    color: var(--title);
    font-size: 21px;
    line-height: 1.3;
    margin-top: 18px;
  }
</style>
</head>
<body>
<main class="stage">
  <section class="card card--front" aria-label="Card front">
    <div class="sports-art" role="img" aria-label="Silhouettes of tennis, basketball and soccer players in action"></div>
    <div class="identity">
      <h1 class="identity__name">DENIZ ARKAN</h1>
      <p class="identity__title">Sports Advisor</p>
      <div class="divider">
        <div class="divider__icons">
          <svg width="24" height="24" viewBox="0 0 24 24" aria-label="Phone">
            <circle cx="12" cy="12" r="11" fill="var(--icon-bg)"/>
            <path d="M8.5 6.5c.6-.4 1.3-.3 1.6.3l1 1.8c.3.5.1 1.1-.3 1.4l-.7.5c.6 1.4 1.6 2.5 3 3.1l.5-.7c.3-.5.9-.6 1.4-.3l1.8 1c.6.3.7 1 .3 1.6l-.7.9c-.6.7-1.6.9-2.5.5-3-1.3-5.3-3.6-6.6-6.6-.4-.9-.2-1.9.5-2.5z" fill="var(--card)"/>
          </svg>
          <svg width="24" height="24" viewBox="0 0 24 24" aria-label="Email">
            <circle cx="12" cy="12" r="11" fill="var(--icon-bg)"/>
            <rect x="6" y="8" width="12" height="8.5" rx="1" fill="none" stroke="var(--card)" stroke-width="1.6"/>
            <path d="M6.4 8.6 12 13l5.6-4.4" fill="none" stroke="var(--card)" stroke-width="1.6"/>
          </svg>
        </div>
      </div>
      <p class="contact">
        +90 555 014 7788<br>
        dnzarkan@mailbox.com
      </p>
      <div class="divider divider--plain"></div>
      <p class="services">
        Betting, Ticket, Soccer,<br>
        Basketball, Tennis Etc
      </p>
    </div>
  </section>

  <section class="card card--back" aria-label="Card back">
    <div class="sports-art" role="img" aria-label="Large silhouettes of tennis, basketball and soccer players in action"></div>
  </section>
</main>
</body>
</html>
```